Wedding Startup Full Website Design

We've just completed our online platform and need to create a website that represents our brand and vision, and clearly communicates our features and value proposition to potential users. There are a minimum of 4 pages that need to be designed. One geared toward wedding professionals (venues/vendors/coordinators), another toward engaged couples, one showcasing features, and an 'About Us' page.

The designer will creative freedom to create a unique UI/UX as long as it represents our brand and is relevant to our target audience/market. The ideal candidate will be able to assume the mindset of someone working in the wedding industry and/or an engaged couple. Ability to create illustrations is a plus.

Copy will be provided as needed. We will reimburse for stock images (pending approval before purchasing), but sourcing the stock images will be the responsibility of the designer.

Our current website: https://www.trelmora.com
Updates

Our project has now been guaranteed! We look forward to finding the perfect design for our site pages!

Still waiting for a design that stands out from the rest and aligns with the creative brief.

Target Market(s)

Wedding Professionals and Engaged Couples

Industry/Entity Type

Wedding

Number of Pages Required

4 page

Font styles to use
Sans Serif

Colors
ffffff
fbd4d5
f59195
33a6d7
cadf82
86cfc6

Requirements
Must have
• Common sense stuff like having a unified brand that accurately represents our platform, speaks to our target market, and clearly articulates our vision
Nice to have
• Illustrations
Should not have
• Overly cheesy or childish. We want to be professional but still embrace the wedding culture.

```html
<!DOCTYPE html>
<html lang="en">
<head>
<meta charset="utf-8">
<title>Trelmora – Smarter Wed Planning</title>
<link href="https://fonts.googleapis.com/css2?family=Poppins:wght@300;400;500;600&display=swap" rel="stylesheet">
<style>
:root{
  --pink:#f59195;
  --pink-soft:#fbd4d5;
  --blue:#33a6d7;
  --ink:#1e1e1e;
  --text:#555;
  --muted:#9a9a9a;
  --grey-bg:#f7f7f7;
  --about-bg:#ececec;
  --footer:#222222;
  --white:#ffffff;
}
*{margin:0;padding:0;box-sizing:border-box}
html,body{width:1200px;height:3696px;overflow:hidden}
body{font-family:"Poppins",sans-serif;color:var(--text);background:var(--white);position:relative}
.abs{position:absolute}

/* hero */
.hero{position:absolute;left:0;top:0;width:1200px;height:892px;background:linear-gradient(100deg,#3f5a2c 0%,#6f7f44 35%,#a58466 62%,#d7a08f 80%,#8f6a55 100%)}
.brand{position:absolute;left:86px;top:40px;font-size:50px;font-weight:400;color:var(--white);letter-spacing:1px}
.nav{position:absolute;top:54px;left:542px;display:flex;gap:0;font-size:16px;font-weight:500;color:var(--white)}
.nav a{color:var(--white);text-decoration:none;padding:0 30px;border-left:1px solid rgba(255,255,255,.7);line-height:16px}
.nav a:first-child{border-left:none;padding-left:0;border-bottom:2px solid var(--pink);padding-bottom:8px}
.social-top{position:absolute;left:996px;top:58px;display:flex;gap:13px}
.dot{width:16px;height:16px;border-radius:50%;background:var(--pink)}
.hero-title{position:absolute;top:276px;width:1200px;text-align:center;font-size:66px;font-weight:400;color:var(--white);letter-spacing:1px}
.hero-sub{position:absolute;top:368px;width:1200px;text-align:center;font-size:30px;font-weight:400;color:var(--white)}
.hero-line{position:absolute;top:390px;width:90px;height:2px;background:var(--pink)}
.btn-start{position:absolute;left:483px;top:456px;width:234px;height:54px;border-radius:27px;background:var(--pink);color:var(--white);font-size:21px;text-align:center;line-height:54px}
.device{position:absolute;left:229px;top:609px;width:747px;height:549px;border-radius:24px;background:linear-gradient(180deg,#f4f6f8 0%,#dfe4ea 52%,#3a4560 53%,#2c3550 100%);box-shadow:0 10px 30px rgba(0,0,0,.25)}

/* how it works */
.how{position:absolute;left:0;top:892px;width:1200px;height:833px;background:var(--grey-bg)}
.sec-title{position:absolute;width:1200px;text-align:center;font-size:52px;font-weight:500;color:var(--ink)}
.title-rule{position:absolute;height:2px;width:150px;background:#cfcfcf}
.title-rule::after{content:"";position:absolute;top:-5px;width:12px;height:12px;border-radius:50%;background:#cfcfcf}
.title-rule.l::after{left:-6px}
.title-rule.r::after{right:-6px}
.step{position:absolute;width:330px;text-align:center}
.step-icon{position:absolute;width:118px;height:118px;border-radius:50%;background:var(--pink);display:flex;align-items:center;justify-content:center}
.step-num{position:absolute;font-size:60px;font-weight:500;color:#dcdcdc}
.step h3{font-size:27px;font-weight:500;color:var(--ink);margin-bottom:14px}
.step p{font-size:15px;line-height:26px;color:var(--text)}
.steps-line{position:absolute;left:180px;top:1533px;width:840px;height:1px;background:#d8d8d8}

/* audiences */
.aud-art{position:absolute;width:170px;height:170px;border-radius:12px;background:linear-gradient(180deg,#fbd4d5,#f59195 70%,#86cfc6)}
.aud-line{position:absolute;top:1971px;height:1px;background:#dcdcdc}
.aud-label{position:absolute;top:1998px;font-size:26px;font-weight:400;color:var(--ink);letter-spacing:1px;text-align:center}

/* about */
.about-photo{position:absolute;left:0;top:2065px;width:586px;height:332px;background:linear-gradient(160deg,#7c8a3a 0%,#b3b35a 45%,#e9e4d6 70%,#6f7a30 100%)}
.about-box{position:absolute;left:609px;top:2065px;width:591px;height:332px;background:var(--about-bg)}
.about-box h2{position:absolute;left:44px;top:46px;font-size:34px;font-weight:400;color:var(--ink)}
.about-box .rule{position:absolute;left:230px;top:73px;width:110px;height:1px;background:#444}
.about-box p{position:absolute;left:44px;top:122px;width:500px;font-size:15px;line-height:30px;color:var(--text)}
.btn-outline{position:absolute;left:41px;top:253px;width:136px;height:37px;border:1px solid #888;border-radius:19px;font-size:14px;text-align:center;line-height:35px;color:var(--ink)}

/* why */
.why-sub{position:absolute;left:160px;top:2586px;width:880px;text-align:center;font-size:15px;line-height:30px;color:#a0a0a0}
.card{position:absolute;top:2725px;width:242px}
.card-img{width:242px;height:136px}
.card-icon{position:absolute;left:81px;top:-40px;width:80px;height:80px;border-radius:50%;background:var(--pink);border:4px solid var(--white);display:flex;align-items:center;justify-content:center}
.card h3{margin-top:24px;text-align:center;font-size:19px;font-weight:400;color:var(--ink);padding-bottom:10px;border-bottom:1px solid #dcdcdc}
.card p{margin-top:12px;text-align:center;font-size:13px;line-height:22px;color:#999}
.arrow{position:absolute;top:2775px;width:28px;height:28px;border-radius:50%;border:1px solid #ccc;display:flex;align-items:center;justify-content:center}

/* features */
.feat{position:absolute;top:3107px;width:325px;height:94px;background:var(--pink);display:flex;align-items:center;color:var(--white)}
.feat svg{margin-left:30px;margin-right:30px;flex:none}
.feat span{font-size:19px;line-height:30px;border-left:1px solid rgba(255,255,255,.6);padding-left:28px}

/* footer */
.footer{position:absolute;left:0;top:3230px;width:690px;height:412px;background:var(--footer);color:#ccc}
.f-brand{position:absolute;left:86px;top:64px;font-size:46px;font-weight:400;color:var(--blue)}
.f-info{position:absolute;left:86px;font-size:13px;line-height:22px;color:#ccc;display:flex;gap:14px;align-items:flex-start}
.f-contact{position:absolute;left:387px;top:55px;font-size:15px;color:var(--white)}
.f-contact::after{content:"";display:block;width:90px;height:1px;background:#666;margin-top:10px}
.f-input{position:absolute;left:387px;width:227px;height:34px;border:1px solid #3a3a3a;background:#1b1b1b;font-size:11px;color:#aaa;padding:0 10px;line-height:32px}
.f-submit{position:absolute;left:387px;top:3482px;width:227px;height:32px;background:#2e2e2e;color:#ddd;font-size:12px;text-align:center;line-height:32px;letter-spacing:1px}
.f-social{position:absolute;left:268px;top:332px;display:flex;gap:10px}
.f-social i{width:15px;height:15px;border-radius:50%;background:#888;display:block}
.f-nav{position:absolute;top:378px;left:0;width:690px;border-top:1px solid #3a3a3a;padding-top:6px;font-size:12px;color:#bbb}
.f-nav a{position:absolute;top:8px;color:#bbb;text-decoration:none}
.map{position:absolute;left:690px;top:3230px;width:510px;height:412px;background:linear-gradient(135deg,#e8e4dc 0%,#d9e6cf 45%,#b8d9a4 55%,#e6e2da 100%)}
.copyright{position:absolute;left:0;top:3642px;width:1200px;height:54px;background:var(--pink);color:var(--white);font-size:13px;text-align:center;line-height:54px}
</style>
</head>
<body>

<header class="hero" role="img" aria-label="Bride with a flower crown in a green garden">
  <div class="brand">Trelmora</div>
  <nav class="nav"><a>About Us</a><a>Features</a><a>For Couples</a></nav>
  <div class="social-top"><i class="dot"></i><i class="dot"></i><i class="dot"></i><i class="dot"></i></div>
  <h1 class="hero-title">Welcome to Trelmora</h1>
  <div class="hero-line" style="left:295px"></div>
  <p class="hero-sub">Smarter Wed Planning</p>
  <div class="hero-line" style="left:815px"></div>
  <div class="btn-start">Get Started</div>
</header>

<section class="how">
  <div class="title-rule l" style="left:250px;top:357px"></div>
  <h2 class="sec-title" style="top:318px">How It Works</h2>
  <div class="title-rule r" style="left:800px;top:357px"></div>
</section>

<div class="device" role="img" aria-label="Tablet with keyboard showing the planning dashboard"></div>

<div class="steps-line"></div>

<div class="step-icon" style="left:190px;top:1350px">
  <svg width="46" height="46" viewBox="0 0 24 24" fill="none" stroke="#fff" stroke-width="2"><circle cx="11" cy="8" r="4"/><path d="M3 21c0-4 4-6 8-6"/><path d="M17 15v6M14 18h6"/></svg>
</div>
<div class="step-num" style="left:250px;top:1420px">.01</div>
<div class="step-icon" style="left:535px;top:1350px">
  <svg width="50" height="50" viewBox="0 0 24 24" fill="#fff"><circle cx="12" cy="8" r="3"/><circle cx="5.5" cy="9.5" r="2.3"/><circle cx="18.5" cy="9.5" r="2.3"/><path d="M7 17c0-3 2.2-5 5-5s5 2 5 5z"/><path d="M1 17c0-2.4 2-4 4.5-4 .8 0 1.4.1 2 .4C6.5 14.5 6 15.7 6 17z"/><path d="M23 17c0-2.4-2-4-4.5-4-.8 0-1.4.1-2 .4 1 1.1 1.5 2.3 1.5 3.6z"/></svg>
</div>
<div class="step-num" style="left:595px;top:1420px">.02</div>
<div class="step-icon" style="left:880px;top:1350px">
  <svg width="46" height="46" viewBox="0 0 24 24" fill="#fff" stroke="#fff" stroke-width="1.6"><circle cx="12" cy="12" r="2.5"/><circle cx="12" cy="3.5" r="1.8"/><circle cx="20" cy="9" r="1.8"/><circle cx="17" cy="20" r="1.8"/><circle cx="7" cy="20" r="1.8"/><circle cx="4" cy="9" r="1.8"/><path d="M12 12V3.5M12 12l8-3M12 12l5 8M12 12l-5 8M12 12L4 9"/></svg>
</div>
<div class="step-num" style="left:940px;top:1420px">.03</div>

<div class="step" style="left:84px;top:1566px"><h3>Sign Up</h3><p>Create a free account on Trelmora to access popular collaboration tools. Get Started</p></div>
<div class="step" style="left:435px;top:1566px"><h3>Collaborate</h3><p>Add clients within the application to better organize and manage event details.</p></div>
<div class="step" style="left:780px;top:1566px"><h3>Connect</h3><p>Linking your bank account within Trelmora to allow for seamless payments and monitoring.</p></div>

<div class="aud-art" style="left:254px;top:1799px" role="img" aria-label="Illustration of an engaged couple under a heart"></div>
<div class="aud-line" style="left:86px;width:500px"></div>
<div class="aud-label" style="left:86px;width:500px">FOR ENGAGED COUPLES</div>
<div class="aud-art" style="left:777px;top:1799px" role="img" aria-label="Illustration of two wedding professionals"></div>
<div class="aud-line" style="left:609px;width:505px"></div>
<div class="aud-label" style="left:609px;width:505px">FOR WEDDING PROFESSIONALS</div>

<div class="about-photo" role="img" aria-label="Bride and groom holding hands in a sunny meadow"></div>
<section class="about-box">
  <h2>About Us</h2><div class="rule"></div>
  <p>Weddings are one the most memorable events in people's life. Unfortunately planning a wedding is filled with stress, often leaving wedding professionals and their clients with soured memories.</p>
  <div class="btn-outline">Learn More</div>
</section>

<div class="title-rule l" style="left:250px;top:2535px"></div>
<h2 class="sec-title" style="top:2494px">Why Trelmora</h2>
<div class="title-rule r" style="left:800px;top:2535px"></div>
<p class="why-sub">We think every wedding and every love story is special. We love weddings, big or small, indoors or outdoors, whatever your dream is.</p>

<div class="arrow" style="left:30px"><svg width="10" height="10" viewBox="0 0 10 10" fill="none" stroke="#aaa" stroke-width="1.5"><path d="M7 1L3 5l4 4"/></svg></div>
<div class="arrow" style="left:1142px"><svg width="10" height="10" viewBox="0 0 10 10" fill="none" stroke="#aaa" stroke-width="1.5"><path d="M3 1l4 4-4 4"/></svg></div>

<div class="card" style="left:86px">
  <div class="card-img" role="img" aria-label="Decorated banquet table with flowers" style="background:linear-gradient(180deg,#6e7a8a,#c9c2b8)"></div>
  <div class="card-icon"><svg width="34" height="34" viewBox="0 0 24 24" fill="none" stroke="#fff" stroke-width="2"><circle cx="12" cy="13" r="8"/><path d="M12 9v4l3 2M9 2h6"/></svg></div>
  <h3>Saves Everyone Time</h3>
  <p>Trelmora streamlines certain processes allowing you to spend more time on the things your want to or just relax!</p>
</div>
<div class="card" style="left:347px">
  <div class="card-img" role="img" aria-label="Couple at an outdoor ceremony" style="background:linear-gradient(180deg,#9aa56a,#e9e6dc)"></div>
  <div class="card-icon"><svg width="34" height="34" viewBox="0 0 24 24" fill="none" stroke="#fff" stroke-width="2"><circle cx="9" cy="14" r="5"/><circle cx="15" cy="11" r="5"/></svg></div>
  <h3>Simplified Organization</h3>
  <p>Trelmora streamlines certain processes allowing you to spend more time on the things your want to or just relax!</p>
</div>
<div class="card" style="left:609px">
  <div class="card-img" role="img" aria-label="Bride sitting in a bright room" style="background:linear-gradient(180deg,#a38d7a,#efe8e0)"></div>
  <div class="card-icon"><svg width="34" height="34" viewBox="0 0 24 24" fill="none" stroke="#fff" stroke-width="2"><path d="M12 3l2.5 5 5.5.8-4 3.9.9 5.5L12 15.6 7.1 18.2 8 12.7 4 8.8l5.5-.8z"/></svg></div>
  <h3>Better Client Reviews</h3>
  <p>Trelmora streamlines certain processes allowing you to spend more time on the things your want to or just relax!</p>
</div>
<div class="card" style="left:870px">
  <div class="card-img" role="img" aria-label="Calendar with a bouquet of flowers" style="background:linear-gradient(180deg,#c9b7a4,#f2efe9)"></div>
  <div class="card-icon"><svg width="34" height="34" viewBox="0 0 24 24" fill="none" stroke="#fff" stroke-width="2"><circle cx="12" cy="12" r="9"/><path d="M3 12h18M12 3c3 3 3 15 0 18M12 3c-3 3-3 15 0 18"/></svg></div>
  <h3>Lower Transaction Fees</h3>
  <p>Trelmora streamlines certain processes allowing you to spend more time on the things your want to or just relax!</p>
</div>

<div class="feat" style="left:86px">
  <svg width="44" height="44" viewBox="0 0 24 24" fill="none" stroke="#fff" stroke-width="1.5"><path d="M2 12l5-5 4 2 4-2 5 5-7 7z"/><path d="M9 14l2 2M11 12l2 2"/></svg>
  <span>Realtime<br>Collaboration</span>
</div>
<div class="feat" style="left:434px">
  <svg width="44" height="44" viewBox="0 0 24 24" fill="none" stroke="#fff" stroke-width="1.5"><path d="M7 17a4 4 0 010-8 6 6 0 0111 1 3.5 3.5 0 010 7z"/><path d="M12 11v8M9 16l3 3 3-3"/></svg>
  <span>Cloud Storage</span>
</div>
<div class="feat" style="left:784px">
  <svg width="44" height="44" viewBox="0 0 24 24" fill="none" stroke="#fff" stroke-width="1.5"><path d="M6 17V11a6 6 0 0112 0v6l2 2H4z"/><path d="M10 21h4"/></svg>
  <span>Notifications &amp;<br>Deadlines</span>
</div>

<footer class="footer">
  <div class="f-brand">Trelmora</div>
  <div class="f-info" style="top:166px"><svg width="12" height="16" viewBox="0 0 12 16" fill="var(--pink)"><path d="M6 0a6 6 0 00-6 6c0 4.5 6 10 6 10s6-5.5 6-10a6 6 0 00-6-6zm0 8.5A2.5 2.5 0 116 3.5a2.5 2.5 0 010 5z"/></svg><span>Address 18 Orchard Lane<br>Maple Ridge, NJ 08000 USA</span></div>
  <div class="f-info" style="top:220px"><svg width="14" height="14" viewBox="0 0 24 24" fill="var(--pink)"><path d="M6.6 10.8a15 15 0 006.6 6.6l2.2-2.2c.3-.3.7-.4 1-.2 1.1.4 2.3.6 3.6.6.6 0 1 .4 1 1V20c0 .6-.4 1-1 1A17 17 0 013 4c0-.6.4-1 1-1h3.5c.6 0 1 .4 1 1 0 1.3.2 2.5.6 3.6.1.3 0 .7-.2 1z"/></svg><span>+1 (555) 014-2287</span></div>
  <div class="f-info" style="top:257px"><svg width="15" height="12" viewBox="0 0 24 18" fill="var(--pink)"><path d="M0 0h24v18H0z"/><path d="M0 0l12 9 12-9" fill="none" stroke="#222" stroke-width="2"/></svg><span>info@trelmora-us.com</span></div>
  <div class="f-contact">Contact Us</div>
  <div class="f-social"><i></i><i></i><i></i><i></i><i></i></div>
  <div class="f-nav">
    <a style="left:129px">Home</a><a style="left:203px">About us</a><a style="left:293px">Services</a><a style="left:381px">Products</a><a style="left:472px">Contact Us</a>
  </div>
</footer>
<div class="f-input" style="top:3346px">Name...</div>
<div class="f-input" style="top:3391px">Email ID...</div>
<div class="f-input" style="top:3436px">Phone No...</div>
<div class="f-submit">SUBMIT</div>

<div class="map" role="img" aria-label="Street map of the office area with location markers"></div>

<div class="copyright">© Copyright 2018, All Rights Reserved</div>

</body>
</html>
```